Managed Service Provider need new business cards

We are a small Maanged Service Provider of IT Services and need a new fresh design for our business cards. We want something impossible, fun and professional :)
Our services has a large range, but we are always fun and make sure our customers both get their issue sorted and also feel like they are "catching up with an old friend".
All our cards in the past has always been all black, with red and we need something fresher.
The back of card, we would like just a small list of what we do i think, but if someone has a better idea, please do something cool with the back of the card:
Managed IT Services
Productivity Solutions
Data Backup and Recovery
IT System Maintenance
Managed IT Security
More details can be found on our website qvtechworks.com.au
Industry/Entity Type
It Company
Contact Information for Business Card
Name: Simon Trelawny
Title: Director
Phone: 03 6158 4932
Mobile: 0417 582 139
Email: simon@qvtechworks.com.au
Web: www.qvtechworks.com.au
Look and feel
Each slider illustrates characteristics of the customer's brand and the style your logo design should communicate.

```html
<!DOCTYPE html>
<html lang="en">
<head>
<meta charset="utf-8">
<title>QV Techworks – Business Card</title>
<link rel="stylesheet" href="https://fonts.googleapis.com/css2?family=Anton&family=Oswald:wght@500&family=Arimo:wght@400&display=swap">
<style>
  :root {
    --brand-red: #ec1c24;
    --ink: #1a1a1a;
    --paper: #ffffff;
    --stage: #2a2a2a;
    --rule: #d4d4d4;
  }
  * { box-sizing: border-box; margin: 0; padding: 0; }
  html, body { width: 1200px; height: 900px; overflow: hidden; }
  body {
    background: var(--stage);
    font-family: "Arimo", Arial, sans-serif;
    position: relative;
  }
  .card {
    position: absolute;
    width: 640px;
    height: 366px;
    left: 280px;
  }
  .card-front {
    top: 64px;
    background: var(--brand-red);
    color: var(--paper);
    display: flex;
    flex-direction: column;
    align-items: center;
    justify-content: center;
    text-align: center;
  }
  .wordmark {
    font-family: "Anton", Impact, sans-serif;
    font-weight: 400;
    letter-spacing: 1px;
    line-height: 1;
  }
  .card-front .wordmark { font-size: 64px; color: var(--paper); }
  .service-list {
    list-style: none;
    margin-top: 34px;
    font-size: 15px;
    line-height: 1.35;
  }
  .service-list .dot {
    display: inline-block;
    width: 7px; height: 7px;
    border-radius: 50%;
    background: var(--paper);
    margin: 0 4px;
    vertical-align: middle;
  }
  .card-back {
    top: 470px;
    background: var(--paper);
    display: flex;
    align-items: center;
  }
  .back-brand {
    width: 340px;
    display: flex;
    justify-content: center;
  }
  .card-back .wordmark { font-size: 44px; color: var(--brand-red); }
  .divider {
    width: 1px;
    height: 150px;
    background: var(--rule);
  }
  .contact {
    padding-left: 34px;
    color: var(--ink);
  }
  .contact-name {
    font-family: "Oswald", sans-serif;
    font-weight: 500;
    font-size: 26px;
    color: var(--brand-red);
    line-height: 1;
  }
  .contact-title { font-size: 16px; margin-bottom: 14px; }
  .contact-list { list-style: none; font-size: 15px; line-height: 1.55; }
  .contact-list li { display: flex; align-items: center; gap: 9px; }
  .contact-list svg { width: 14px; height: 14px; flex: none; }
  .accent { color: var(--brand-red); }
</style>
</head>
<body>
  <section class="card card-front">
    <div class="wordmark">QV TECHWORKS</div>
    <ul class="service-list">
      <li>Data Backup and Recovery</li>
      <li>IT System Maintenance<span class="dot"></span>Productivity Solutions</li>
      <li>Managed IT Security<span class="dot"></span>Managed IT Services</li>
    </ul>
  </section>

  <section class="card card-back">
    <div class="back-brand"><div class="wordmark">QV TECHWORKS</div></div>
    <div class="divider"></div>
    <div class="contact">
      <div class="contact-name">SIMON TRELAWNY</div>
      <div class="contact-title">Director</div>
      <ul class="contact-list">
        <li>
          <svg viewBox="0 0 24 24"><path fill="#ec1c24" d="M6.6 10.8a15 15 0 0 0 6.6 6.6l2.2-2.2c.3-.3.7-.4 1-.2 1.1.4 2.3.6 3.6.6.6 0 1 .4 1 1V20c0 .6-.4 1-1 1A17 17 0 0 1 3 4c0-.6.4-1 1-1h3.5c.6 0 1 .4 1 1 0 1.3.2 2.5.6 3.6.1.3 0 .7-.2 1z"/></svg>
          03 6158 4932
        </li>
        <li>
          <svg viewBox="0 0 24 24"><rect x="6" y="2" width="12" height="20" rx="2" fill="none" stroke="#ec1c24" stroke-width="2.5"/><circle cx="12" cy="18" r="1.3" fill="#ec1c24"/></svg>
          0417 582 139
        </li>
        <li>
          <svg viewBox="0 0 24 24"><rect x="2" y="5" width="20" height="14" fill="#ec1c24"/><path d="M2 5l10 8 10-8" fill="none" stroke="#fff" stroke-width="1.6"/></svg>
          simon@qvtechworks.com.au
        </li>
        <li>
          <svg viewBox="0 0 24 24"><g fill="none" stroke="#ec1c24" stroke-width="2"><circle cx="12" cy="12" r="9.5"/><ellipse cx="12" cy="12" rx="4" ry="9.5"/><path d="M2.5 12h19M4 7h16M4 17h16"/></g></svg>
          <span>www.<span class="accent">qvtechworks</span>.com.au</span>
        </li>
      </ul>
    </div>
  </section>
</body>
</html>
```